Poem Handwritten by Veteran while in the jungle of Vietnam

My parents are celebrating their 50th wedding anniversary this year. I wanted to give them a very memorable gift. On my parents 2nd anniversary, my father was stationed in Vietnam. On that night he was in the jungle waiting till morning and wrote a poem to my mother using his pant leg as paper. I would like this poem to typographically designed to be framed and hung on the wall.

I have attached a picture of the poem below. It will need to be 11x14 when printed for framing. It would be great if there was background or artwork to make it more visually interesting, perhaps in a watercolor. My parents have a transitional style. I have attached some possible color schemes as well. Cool greens, blue, neutral grays, with hints of berries or highlights of yellow. These are just a guide, I would be open to your interpretations.

Thank you for your help. This will hopefully be a gift they will truly treasure as much as the poem itself.

Target Market(s)

My parents who are excited to be celebrating their 50th wedding anniversary. It should have a transitional, mature style.

Font styles to use
Serif
Script

Requirements
Must have
• The poem, typographically designed. There can be a mix of fonts, but legibility is critically important.
• Now that some designs have come through I wanted to give some more guidance of what I'm looking for. I want something that feels sophisticated and artistic.
Nice to have
• A background or art work, using the color schemes attached as a guide. I am really liking the designs that have a full color landscape artwork in the background. The fonts should be elegant and formal. I really like the romantic, muted colors. I had trouble finding similar projects online in the style I wanted until I cam across wedding invites. Those seem to be the most applicable. I've added pictures of some so you can get a sense of what I'm looking for. I am really liking the jungle foliage, starry skies or sunrises.
Should not have
• Cartoon caricatures, fonts that are too illegible when printed. I'm not liking anything whimsical. I don't like the very bright colors for this project.

```html
<!DOCTYPE html>
<html lang="en">
<head>
<meta charset="utf-8">
<title>Walter's Anniversary Poem</title>
<link rel="stylesheet" href="https://fonts.googleapis.com/css2?family=Stardos+Stencil:wght@700&family=Parisienne&display=swap">
<style>
  :root {
    --sky-dark: #2b2b2a;
    --sky-mid: #6b6a66;
    --mist: #a9a7a1;
    --forest: #1f211e;
    --ink-light: #ffffff;
    --ink-shadow: rgba(0, 0, 0, 0.85);
    --ornament-dark: rgba(20, 20, 20, 0.55);
    --ornament-light: rgba(255, 255, 255, 0.35);
    --rule: rgba(255, 255, 255, 0.75);
  }
  html, body {
    margin: 0;
    padding: 0;
    width: 980px;
    height: 1200px;
    overflow: hidden;
    background: #eeeeee;
  }
  .poster {
    position: relative;
    width: 980px;
    height: 1200px;
    overflow: hidden;
    background: var(--sky-dark);
  }
  .landscape {
    position: absolute;
    inset: 0;
    background:
      radial-gradient(ellipse 60% 35% at 65% 48%, rgba(190, 188, 182, 0.7), transparent 70%),
      radial-gradient(ellipse 50% 25% at 30% 30%, rgba(150, 148, 142, 0.45), transparent 70%),
      linear-gradient(to bottom,
        var(--sky-dark) 0%,
        #4a4946 14%,
        var(--sky-mid) 32%,
        var(--mist) 50%,
        #8d8b86 66%,
        #4c4d49 80%,
        var(--forest) 100%);
  }
  .ornament {
    position: absolute;
    border-radius: 50%;
  }
  .ornament--upper {
    left: 560px;
    top: 262px;
    width: 330px;
    height: 262px;
    background: radial-gradient(ellipse at center, var(--ornament-dark), transparent 70%);
  }
  .ornament--lower {
    left: 112px;
    top: 936px;
    width: 314px;
    height: 155px;
    background: radial-gradient(ellipse at center, var(--ornament-light), transparent 70%);
  }
  .title-block {
    position: absolute;
    left: 60px;
    top: 61px;
    width: 860px;
    height: 116px;
    border-top: 2px solid var(--rule);
    border-bottom: 2px solid var(--rule);
    text-align: center;
  }
  .title {
    margin: 0;
    padding-top: 20px;
    font-family: "Stardos Stencil", serif;
    font-weight: 700;
    font-size: 35px;
    line-height: 42px;
    letter-spacing: 0.5px;
    color: var(--ink-light);
    text-transform: uppercase;
  }
  .poem-column {
    position: absolute;
    width: 460px;
    text-align: center;
    font-family: "Parisienne", cursive;
    font-size: 23px;
    line-height: 22.5px;
    color: var(--ink-light);
    text-shadow: 1px 1px 1px var(--ink-shadow), 0 0 3px var(--ink-shadow);
  }
  .poem-column--left {
    left: 28px;
    top: 236px;
  }
  .poem-column--right {
    left: 498px;
    top: 598px;
  }
  .stanza {
    margin: 0 0 27px;
  }
  .stanza:last-child {
    margin-bottom: 0;
  }
</style>
</head>
<body>
<main class="poster">
  <div class="landscape" role="img" aria-label="Misty grey sky over a dark forest treeline"></div>
  <div class="ornament ornament--upper" role="img" aria-label="Dark leafy flourish ornament"></div>
  <div class="ornament ornament--lower" role="img" aria-label="White swirling flourish ornament"></div>

  <header class="title-block">
    <h1 class="title">20 July 1070, Monday, LZ Meridian<br>Walter's Anniversary Poem</h1>
  </header>

  <section class="poem-column poem-column--left">
    <p class="stanza">Life's journey began with a challenge,<br>It was heralded far and near.<br>The road led on forever,<br>Its completion was known to be dear.</p>
    <p class="stanza">From the garden of light it proceeded,<br>To the valley of shadows it led.<br>Thorns and thistles adorned it,<br>Past abyss and crevice it sped.</p>
    <p class="stanza">The brave surged forward with courage,<br>The wise undaunted pressed on.<br>The mighty held high their banner,<br>We all awaited the dawn.</p>
    <p class="stanza">Though the pitfalls and hazards were many,<br>The pathway was clearly in view.<br>Straight and sure it glided,<br>Its course we knew to be true.</p>
    <p class="stanza">I knew you, Sweetheart, beforehand,<br>So precious and sweet were you.<br>Our moments of bliss were priceless,<br>Each day brought us joy anew.</p>
    <p class="stanza">The call to progression beckoned,<br>At last I would have my chance &ndash;<br>To clasp you to me forever,<br>And seal our divine romance.</p>
  </section>

  <section class="poem-column poem-column--right">
    <p class="stanza">I eagerly started the journey,<br>Though with sorrow, I left you behind.<br>With courage and faith I continued,<br>For I knew, that you later I'd find.</p>
    <p class="stanza">I diligently searched for you, Darling,<br>The roadway was both bleak and fair.<br>Though the years grew long in number,<br>I did not give up in despair.</p>
    <p class="stanza">At last in the distance I saw you,<br>So beautiful, lovely, and sweet!<br>Your attention I struggled to capture,<br>Your love I wrested to meet.</p>
    <p class="stanza">What rapture was mine in fulfillment,<br>As now together we stand.<br>To cherish and love each other,<br>While our plans and dreams expand.</p>
    <p class="stanza">I love you, Darling, forever,<br>My life you have made replete.<br>Our eternal mansion bekons,<br>Your love has made it complete.</p>
  </section>
</main>
</body>
</html>
```